Property Management Company Business Cards

Need business cards for a property management company located in Michigan. We manage houses for clients all over the world. Young and modern company, looking for eye catching design. Please work with the attached logo.

Industry/Entity Type

Property Management

Requirements
Must have
• Need lines for address, telephone number, fax number, web site.

Also lines for name, and job title

```html
<!DOCTYPE html>
<html lang="en">
<head>
<meta charset="utf-8">
<title>Lakeview Harbor Management – Business Card</title>
<link rel="stylesheet" href="https://fonts.googleapis.com/css2?family=Arimo:wght@400;700&display=swap">
<style>
  :root {
    --card-cyan: #4fdcff;
    --band-grey: #7f9ba1;
    --brand-tint: #5ce2ff;
    --ink: #22363c;
  }
  * { margin: 0; padding: 0; box-sizing: border-box; }
  html, body { width: 1200px; height: 720px; overflow: hidden; background: var(--card-cyan); }
  .card {
    position: relative;
    width: 1200px;
    height: 720px;
    overflow: hidden;
    background: var(--card-cyan);
    font-family: "Arimo", Arial, sans-serif;
    color: var(--ink);
  }
  .side-band {
    position: absolute; left: 0; top: 0;
    width: 137px; height: 720px;
    background: var(--band-grey);
  }
  .brand-name {
    position: absolute; left: 160px; top: 138px;
    color: var(--brand-tint);
    font-weight: 700;
    font-size: 58px;
    line-height: 66px;
    white-space: nowrap;
  }
  .holder {
    position: absolute; left: 160px; top: 406px; width: 310px;
    text-align: center; font-size: 49px; line-height: 62px;
    white-space: nowrap;
  }
  .divider {
    position: absolute; left: 526px; top: 398px;
    width: 2px; height: 162px; background: var(--ink);
  }
  .contact {
    position: absolute; left: 590px; top: 392px;
    font-size: 32px; line-height: 43px;
    border-collapse: collapse;
  }
  .contact th { font-weight: 400; text-align: left; padding: 0 22px 0 0; width: 153px; }
  .contact td { padding: 0; white-space: nowrap; }
</style>
</head>
<body>
<div class="card">
  <div class="side-band"></div>

  <p class="brand-name">LAKEVIEW HARBOR MANAGEMENT</p>

  <div class="holder">
    <p class="holder-name">Daniel Reyes</p>
    <p class="holder-title">Director</p>
  </div>

  <div class="divider"></div>

  <table class="contact">
    <tr><th>adress:</th><td>48 Birch Lane, MI</td></tr>
    <tr><th>phone:</th><td>012 345 678 9</td></tr>
    <tr><th>fax:</th><td>012 345 678 0</td></tr>
    <tr><th>website:</th><td>www.lakeviewharbor.com</td></tr>
  </table>
</div>
</body>
</html>
```